Corbel Crest Lighting - Commercial & Residential Landscape Lighting

Landscape Lighting Services & Design: Create a website for our landscape lighting company. We would like the design to be tailored around this description:
Illuminate with Confidence. Designed with Precision. Installed with Care.
Locally and veteran-owned, we take pride in transforming outdoor spaces through innovative lighting solutions tailored to your vision. From landscape and holiday lighting to permanent installations, our effortless process and expert design deliver breathtaking results and lasting curb appeal. Backed by a lifetime warranty and quarterly service options, our commitment to quality and customer satisfaction is unwavering. Try before you buy and experience your home in a whole new light with our complimentary demo kit — see the stunning effects before you decide.
- Also, add in this information as well; Outdoor Lighting not only beautifies spaces but also significantly enhances safety by illuminating your home or business. Beautifully lit entrances deter potential intruders, making your home a safer place for your loved ones. we also offer quarterly service plans to ensure lighting equipment continues to operate & illuminate effectively throughout the year. Also mention we provide free estimates and we are offering a 10% discount to military, veterans, and first responders.

Target Market(s)

Luxury market

Industry/Entity Type

Landscape Lighting - Residential & Commercial Lighting Services

Coding

Coded - Design and coding required

Number of Pages Required

2 page

Colors
00AB8E
00BBA5
67D7C9
C6EFE9
E9F9F6
59FF00
82FF00
B8FF75
E3FFCB
F4FFEA
FFC000
F8CF3A
FAE287
FDF2CF
FEFAEE

Requirements
Must have
• a lead generation button where people can submit their information for us to reach out to them and schedule their free estimate, homepage, about page, contact page, products and services page, user friendly, easy to navigate, and it also must be engaging and eye popping, as well as appealing to the luxury market. Please use colors; verdent green, dark green, ivory, and sunny yellow. Also, include an about page that references our story; Glen is retired Army and he opened a fitness studio in 2017 with his wife Rosalind. He has installed low voltage lighting in every home he lived in and for his friends and family over the years and decided to open his own business because he is passionate about beautifying outdoor landscapes and highlighting a properties full potential, not only in the day but at night as well all while providing safety and security for his clients. Having a deep respect for nature and landscaping, he wants to provide the same care and quality to each of his clients as he has in the fitness industry for decades. He believes small businesses are the back bone of America and he's excited to provide a service that is all to often neglected in the design of a home.
Nice to have
• I would like to have a clear intent and purpose, engaging web design, clear call to action, optimized for search engines, mobile friendy design, security measures, credibility indicators

```html
<!DOCTYPE html>
<html lang="en">
<head>
<meta charset="utf-8">
<title>Corbel Crest Lighting — Landscape Lighting</title>
<link href="https://fonts.googleapis.com/css2?family=Inter:wght@400;500;600;700;800&display=swap" rel="stylesheet">
<style>
:root{
  --yellow:#F8C51C;
  --yellow-soft:#FAE287;
  --cream:#FDF2CF;
  --ivory:#FEFAEE;
  --green:#00AB8E;
  --green-bright:#59FF00;
  --green-dark:#0E2A22;
  --ink:#1c1c1c;
  --text:#5b5b5b;
  --grey-tile:#f5f5f5;
}
*{box-sizing:border-box;margin:0;padding:0}
html,body{width:1200px;height:4144px;overflow:hidden}
body{position:relative;background:#fff;font-family:"Inter",sans-serif;color:var(--ink)}
.abs{position:absolute}
.btn{position:absolute;display:flex;align-items:center;gap:8px;justify-content:center;background:var(--yellow);color:#2a1e00;font-weight:600;font-size:12px;border-radius:3px;text-decoration:none;white-space:nowrap}
.btn .arr{width:14px;height:14px;border:1.5px solid #2a1e00;border-radius:50%;display:flex;align-items:center;justify-content:center;font-size:9px;line-height:1}
.photo{position:absolute;border-radius:6px;overflow:hidden}
h2.sec{position:absolute;font-weight:700;font-size:29px;line-height:1.2;color:var(--ink)}
p.body{position:absolute;font-size:11px;line-height:18px;color:var(--text)}

/* Header + hero */
.hero{position:absolute;left:0;top:0;width:1200px;height:637px;background:linear-gradient(180deg,#2c3346 0%,#3a3a40 30%,#7a4a1c 55%,#3a2c1e 78%,#2a2a26 100%)}
.brand{position:absolute;left:150px;top:26px;color:var(--yellow);font-weight:600;font-size:26px;letter-spacing:1px}
.nav{position:absolute;left:423px;top:27px;width:345px;height:28px;border:1px solid rgba(255,255,255,.55);border-radius:3px;display:flex;align-items:center;padding:0 3px;gap:2px;background:rgba(255,255,255,.12)}
.nav a{color:#fff;text-decoration:none;font-size:11px;font-weight:500;padding:4px 11px;border-radius:2px}
.nav a.on{background:rgba(255,255,255,.35)}
.hero-card{position:absolute;left:153px;top:209px;width:450px;height:237px;background:rgba(40,32,28,.72);border-radius:8px}
.hero-card h1{position:absolute;left:22px;top:12px;color:#fff;font-size:42px;line-height:57px;font-weight:700;white-space:nowrap}
.hero-card p{position:absolute;left:22px;top:128px;width:412px;color:#eee;font-size:11px;line-height:18px}
.play{position:absolute;left:846px;top:228px;width:200px;height:200px}
.hero-note{position:absolute;top:573px;color:#fff;font-size:11px;line-height:16px;padding-left:10px;border-left:1px solid rgba(255,255,255,.7);white-space:nowrap}
.slider{position:absolute;left:0;top:576px;width:138px;height:61px;background:#fff;display:flex;align-items:center;justify-content:center;gap:12px;font-size:12px;font-weight:600}
.dot{width:8px;height:8px;border-radius:50%;border:1px solid #ddd}

/* Services tabs */
.tabs{position:absolute;left:314px;top:1111px;width:572px;height:30px;background:var(--ivory);display:flex;align-items:center;font-size:11px;color:#333}
.tabs span{padding:0 15px;height:30px;display:flex;align-items:center}
.tabs span.on{background:var(--yellow-soft);padding:0 24px}
.chip{position:absolute;left:58px;bottom:0;background:var(--yellow-soft);padding:8px 14px;font-size:17px;font-weight:500;border-radius:4px 4px 0 0}
.circ{position:absolute;width:22px;height:22px;border-radius:50%;border:1px solid #999;display:flex;align-items:center;justify-content:center;font-size:12px;color:#555}

/* Grid tiles */
.tile{position:absolute;width:176px;height:180px;background:var(--grey-tile);text-align:center}
.tile .pic{position:absolute;left:53px;top:18px;width:70px;height:80px;border-radius:6px}
.tile .nm{position:absolute;left:0;right:0;top:119px;font-size:12px;font-weight:600}
.tile .pr{position:absolute;left:0;right:0;top:139px;font-size:16px;font-weight:700;color:var(--green)}
.tile.hi{background:var(--yellow)}
.tile.soft{background:var(--cream)}

.panel{position:absolute;left:150px;width:899px;background:var(--ivory);border-radius:10px}
.pcard{position:absolute;top:90px;width:187px;height:180px;background:#fff;border-radius:4px;text-align:center}
.pcard .pic{position:absolute;left:44px;top:15px;width:100px;height:80px;border-radius:6px}
.pcard .nm{position:absolute;left:0;right:0;top:122px;font-size:12px;font-weight:600}
.pcard .pr{position:absolute;left:0;right:0;top:142px;font-size:16px;font-weight:700;color:var(--green)}

.ccard{position:absolute;left:19px;width:412px;background:var(--cream);border-radius:6px}
.ccard svg{position:absolute;left:18px;top:18px}
.ccard b{position:absolute;left:52px;top:12px;font-size:14px;font-weight:600}
.ccard small{position:absolute;left:52px;top:36px;font-size:11px;color:var(--text)}

.footer{position:absolute;left:0;top:3753px;width:1200px;height:391px;background:var(--green-dark);color:#fff}
.fcol{position:absolute;top:177px;font-size:11px}
.fcol h4{font-size:14px;font-weight:500;margin-bottom:12px}
.fcol li{list-style:none;line-height:22px;color:#dfe9e4}
.soc{position:absolute;top:311px;width:30px;height:30px;border-radius:50%;background:#fff}
</style>
</head>
<body>

<!-- Hero -->
<section class="hero" role="img" aria-label="Historic building facade lit with warm lights at dusk, with a plaza and benches in front">
  <div class="brand">CORBEL CREST</div>
  <nav class="nav"><a class="on">Home</a><a>About</a><a>Services</a><a>Products</a><a>Contact</a></nav>
  <a class="btn" href="#estimate" style="left:920px;top:26px;width:129px;height:34px">Get In Touch <span class="arr">→</span></a>
  <div class="hero-card">
    <h1>Premier Landscape<br>Lighting Specialist</h1>
    <p>Illuminate With Confidence. Designed With Precision. Installed With Care. Free Estimates And A Lifetime Warranty On Every Install.</p>
    <a class="btn" href="#estimate" style="left:22px;top:180px;width:178px;height:34px">Request Free Estimate <span class="arr">→</span></a>
  </div>
  <svg class="play" viewBox="0 0 200 200">
    <path d="M100 12 A88 88 0 0 1 150 172" fill="none" stroke="#F8C51C" stroke-width="6" stroke-linecap="round"/>
    <path d="M112 28 A74 74 0 0 1 140 160" fill="none" stroke="#F8C51C" stroke-width="3" opacity=".7"/>
    <path d="M86 82 L122 100 L86 118 Z" fill="#fff" stroke="#fff" stroke-width="6" stroke-linejoin="round"/>
  </svg>
  <div class="hero-note" style="left:643px">Lifetime Warranty And<br>Quarterly Service Plans</div>
  <div class="hero-note" style="left:869px">10% Off For Military, Veterans<br>And First Responders.</div>
  <div class="slider"><span>←</span><span>01</span><span class="dot"></span><span>→</span></div>
</section>

<!-- About -->
<section>
  <div class="photo" style="left:256px;top:727px;width:212px;height:177px;background:linear-gradient(180deg,#5a6a7a,#b3743a 60%,#5a6d2c)" role="img" aria-label="House with warm landscape lighting at dusk"></div>
  <div class="photo" style="left:150px;top:788px;width:212px;height:179px;background:linear-gradient(180deg,#6f8aa5,#c48850 55%,#4b5a32)" role="img" aria-label="Home exterior lit at twilight"></div>
  <div class="photo" style="left:430px;top:770px;width:178px;height:179px;background:linear-gradient(180deg,#2c3c50,#9c5a2c 55%,#2f3a22)" role="img" aria-label="Lit house facade with lawn at night"></div>
  <h2 class="sec" style="left:663px;top:733px">Corbel Crest Lighting Is<br>What We Do Everyday.</h2>
  <p class="body" style="left:663px;top:816px;width:388px">Locally And Veteran-Owned, Corbel Crest Brings Over 30 Years Of Experience In Outdoor Lighting Design And Installation. Try Before You Buy With Our Complimentary Demo Kit. Beautifully Lit Entrances Deter Intruders And Keep Your Loved Ones Safe.</p>
  <div class="btn" style="left:663px;top:920px;width:120px;height:33px">Know More <span class="arr">→</span></div>
</section>

<!-- Popular services -->
<section>
  <h2 class="sec" style="left:0;width:1200px;text-align:center;top:1050px">POPULAR SERVICES</h2>
  <div class="tabs"><span class="on">Landscape Lighting</span><span>Outdoor Audio</span><span>Permanent Roofline Lighting</span><span>Maintenance</span></div>
  <div class="photo" style="left:150px;top:1173px;width:284px;height:214px;background:linear-gradient(180deg,#2a3e6e,#5a6b9a 45%,#2a2a34)" role="img" aria-label="Outdoor patio with screen and garden lighting at night">
    <div class="chip">Landscape Lighting</div>
  </div>
  <div class="photo" style="left:457px;top:1173px;width:285px;height:214px;background:linear-gradient(160deg,#9cc4e4,#cbdbe6 50%,#7a8a5a)" role="img" aria-label="Outdoor speaker mounted among foliage"></div>
  <div class="photo" style="left:764px;top:1173px;width:285px;height:214px;background:linear-gradient(180deg,#0e1a2c,#5a2a14 55%,#8a3a18)" role="img" aria-label="House roofline with permanent warm lighting at night"></div>
  <div class="circ" style="left:574px;top:1418px">‹</div>
  <div class="circ" style="left:604px;top:1418px;border-color:#333;color:#333">›</div>
</section>

<!-- Lighting solutions -->
<section>
  <h2 class="sec" style="left:150px;top:1526px">Lighting Solutions</h2>
  <p class="body" style="left:150px;top:1573px;width:300px">From The Initial Design Consultation To The Final Walkthrough, We Bring Over 30 Years Of Expertise To Transforming Your Outdoor Space With Stunning, Functional Lighting. Our Team Carefully Plans Every Detail, Ensuring A Flawless Installation That Enhances Your Home's Beauty, Security, And Curb Appeal. From Landscape And Holiday Lighting To Permanent Installations, These Options Give You Design Flexibility. Our Quarterly Service Plans Keep Every Fixture Operating And Illuminating Effectively Throughout The Year. Not Sure Which Fixture Works Best For Your Space? Try Our Free Demo Kit And See The Stunning Effect Before You Decide.</p>
  <div class="btn" style="left:150px;top:1861px;width:170px;height:34px">Explore All Products <span class="arr">→</span></div>

  <div class="tile" style="left:519px;top:1533px"><div class="pic" style="background:radial-gradient(circle,#555,#ddd 70%)" role="img" aria-label="Black spotlight fixture"></div><div class="nm">Eclipse Solar Path Light</div><div class="pr">$179.99</div></div>
  <div class="tile hi" style="left:696px;top:1533px"><div class="pic" style="background:radial-gradient(circle,#333,#F8C51C 70%)" role="img" aria-label="Hanging black lantern"></div><div class="nm">Serenity Solar Lantern</div><div class="pr">$349.99</div></div>
  <div class="tile" style="left:873px;top:1533px"><div class="pic" style="background:radial-gradient(circle,#222,#ddd 70%)" role="img" aria-label="Black wall-mounted outdoor light"></div><div class="nm">Outdoor Solar Light</div><div class="pr">$179.99</div></div>
  <div class="tile" style="left:519px;top:1717px"><div class="pic" style="background:radial-gradient(circle,#444,#ddd 70%)" role="img" aria-label="Set of modern pendant lights"></div><div class="nm">Modern Pendant Lights</div><div class="pr">$179.99</div></div>
  <div class="tile soft" style="left:696px;top:1717px"><div class="pic" style="background:radial-gradient(circle,#4a6a5a,#FDF2CF 70%)" role="img" aria-label="Stacked geometric light fixture"></div><div class="nm">Eclipse Solar Path Light</div><div class="pr">$179.99</div></div>
  <div class="tile" style="left:873px;top:1717px"><div class="pic" style="background:radial-gradient(circle,#555,#ddd 70%)" role="img" aria-label="Black spotlight fixture"></div><div class="nm">Eclipse Solar Path Light</div><div class="pr">$179.99</div></div>
</section>

<!-- Products -->
<section class="panel" style="top:1995px;height:352px;overflow:hidden">
  <h2 class="sec" style="left:0;width:899px;text-align:center;top:29px">Our Products</h2>
  <div class="pcard" style="left:24px"><div class="pic" style="background:radial-gradient(ellipse,#fff,#cfcfcf 75%)" role="img" aria-label="White flush ceiling light"></div><div class="nm">Eclipse Solar Path Light</div><div class="pr">$179.99</div></div>
  <div class="pcard" style="left:235px"><div class="pic" style="background:radial-gradient(ellipse,#333,#e6e6e6 70%)" role="img" aria-label="Black wall spot light"></div><div class="nm">Eclipse Solar Path Light</div><div class="pr">$179.99</div></div>
  <div class="pcard" style="left:446px"><div class="pic" style="background:radial-gradient(ellipse,#888,#eee 70%)" role="img" aria-label="Twin white spot lights"></div><div class="nm">Eclipse Solar Path Light</div><div class="pr">$179.99</div></div>
  <div class="pcard" style="left:657px"><div class="pic" style="background:radial-gradient(ellipse,#f4e6c8,#c8a86a 75%)" role="img" aria-label="Gold ring ceiling light"></div><div class="nm">Eclipse Solar Path Light</div><div class="pr">$179.99</div></div>
  <div class="pcard" style="left:868px"></div>
  <div class="abs" style="left:782px;top:296px;display:flex;gap:12px;align-items:center;font-size:12px;font-weight:600"><span>←</span><span>01</span><span class="dot"></span><span>→</span></div>
</section>

<!-- Story -->
<section>
  <div class="photo" style="left:201px;top:2437px;width:343px;height:124px;border-radius:4px;background:linear-gradient(180deg,#3a4a6e,#a06030 60%,#3a2a1a)" role="img" aria-label="Grand building illuminated at night"></div>
  <div class="photo" style="left:378px;top:2497px;width:130px;height:125px;border-radius:4px;background:linear-gradient(180deg,#1a2a4a,#3a5a8a 50%,#c08a3a)" role="img" aria-label="Lit trees along a curved path at night"></div>
  <div class="photo" style="left:150px;top:2580px;width:270px;height:224px;border-radius:4px;background:linear-gradient(180deg,#14244a,#2a3a5a 45%,#9a6a30 80%,#2a2018)" role="img" aria-label="Modern home with lit outdoor steps"></div>
  <div class="photo" style="left:420px;top:2580px;width:124px;height:161px;border-radius:4px;background:linear-gradient(180deg,#5a6a8a,#c8a070 55%,#3a3a3a)" role="img" aria-label="Lit historic building at dusk"></div>
  <h2 class="sec" style="left:587px;top:2480px">Our Story</h2>
  <p class="body" style="left:587px;top:2525px;width:460px">Glen Is Retired Army And He Opened A Fitness Studio In 2017 With His Wife Rosalind. He Has Installed Low Voltage Lighting In Every Home He Lived In And For His Friends And Family Over The Years And Decided To Open His Own Business Because He Is Passionate About Beautifying Outdoor Landscapes And Highlighting A Properties Full Potential, Not Only In The Day But At Night As Well All While Providing Safety And Security For His Clients. Having A Deep Respect For Nature And Landscaping, He Wants To Provide The Same Care And Quality To Each Of His Clients As He Has In The Fitness Industry For Decades. He Believes Small Businesses Are The Back Bone Of America And He's Excited To Provide A Service That Is All To Often Neglected In The Design Of A Home.</p>
  <div class="btn" style="left:587px;top:2723px;width:118px;height:34px">Explore All <span class="arr">→</span></div>
</section>

<!-- Contact -->
<section class="panel" id="estimate" style="top:2896px;height:378px">
  <h2 class="sec" style="left:19px;top:22px">Contact Us</h2>
  <div class="ccard" style="top:72px;height:61px">
    <svg width="18" height="20" viewBox="0 0 18 20"><path d="M9 1a6 6 0 0 0-6 6c0 5 6 11 6 11s6-6 6-11a6 6 0 0 0-6-6z" fill="none" stroke="#333" stroke-width="1.6"/><circle cx="9" cy="7" r="2" fill="#333"/></svg>
    <b>Our Location</b><small>482 Lantern Ridge Road, Aldermoor, Texas 78209, United States</small>
  </div>
  <div class="ccard" style="top:149px;height:64px">
    <svg width="20" height="20" viewBox="0 0 20 20"><path d="M4 2l4 1 1 4-2 2a11 11 0 0 0 4 4l2-2 4 1 1 4-2 2C8 18 2 12 2 4z" fill="none" stroke="#333" stroke-width="1.6" stroke-linejoin="round"/></svg>
    <b>Our Phone</b><small>210-555-0148</small>
  </div>
  <div class="ccard" style="top:230px;height:62px">
    <svg width="22" height="18" viewBox="0 0 22 18"><rect x="1" y="2" width="20" height="14" rx="2" fill="none" stroke="#333" stroke-width="1.6"/><path d="M1 3l10 7 10-7" fill="none" stroke="#333" stroke-width="1.6"/></svg>
    <b>Email Address</b><small>Hello@CorbelCrest.Com</small>
  </div>
  <div class="abs" style="left:19px;top:318px;font-size:14px;font-weight:500">Hours Of Operation</div>
  <div class="abs" style="left:19px;top:339px;font-size:11px;color:var(--text)">Monday-Sunday : 08:00Am To 07:00Pm</div>
  <div class="abs" style="left:469px;top:19px;width:411px;height:342px;border-radius:4px;background:linear-gradient(135deg,#b9d3e6,#dfe6e0 45%,#9cc2da)" role="img" aria-label="Street map of the business location"></div>
</section>

<!-- Featured projects -->
<section>
  <h2 class="sec" style="left:0;width:1200px;text-align:center;top:3360px">Our Featured Projects</h2>
  <div class="abs" style="left:0;width:1200px;text-align:center;top:3400px;font-size:11px;color:var(--text)">Discover Corbel Crest's Low Voltage Landscape Lighting With Accent Lighting</div>
  <div class="photo" style="left:0;top:3442px;width:246px;height:189px;border-radius:3px;background:linear-gradient(180deg,#4a5a6e,#b0703a 45%,#3a5a24)" role="img" aria-label="House with lit front lawn"></div>
  <div class="photo" style="left:269px;top:3442px;width:159px;height:189px;border-radius:3px;background:linear-gradient(180deg,#2a3a4e,#a0683a 50%,#2a3a1e)" role="img" aria-label="House lit at night"></div>
  <div class="photo" style="left:450px;top:3442px;width:298px;height:189px;border-radius:3px;background:linear-gradient(180deg,#2a3a2a,#8a6a3a 50%,#5a6a3a)" role="img" aria-label="Modern garden pathway with step lights"></div>
  <div class="photo" style="left:769px;top:3442px;width:159px;height:189px;border-radius:3px;background:linear-gradient(180deg,#3a4e6e,#b07a4a 50%,#3a4a2a)" role="img" aria-label="Lit house at twilight"></div>
  <div class="photo" style="left:951px;top:3442px;width:249px;height:189px;border-radius:3px;background:linear-gradient(180deg,#2a1a12,#8a4a22 50%,#2a1e12)" role="img" aria-label="Lit home entrance with garden at night"></div>
  <div class="abs" style="left:87px;top:3659px;width:1025px;height:2px;background:#e2e2e2"></div>
  <div class="abs" style="left:87px;top:3658px;width:204px;height:3px;background:var(--yellow)"></div>
</section>

<!-- Footer -->
<footer class="footer">
  <div class="abs" style="left:0;width:1200px;text-align:center;top:48px;color:var(--yellow);font-size:34px;font-weight:600;letter-spacing:1px">CORBEL CREST</div>
  <div class="abs" style="left:257px;top:142px;width:686px;height:1px;background:rgba(255,255,255,.35)"></div>
  <div class="fcol" style="left:257px"><h4>Quick Links</h4><ul><li>Home</li><li>About Us</li><li>Product</li><li>Contact Us</li></ul></div>
  <div class="fcol" style="left:433px"><h4>Services</h4><ul><li>Landscape Lighting</li><li>Outdoor Audio</li><li>Permanent Roofline Lighting</li><li>Maintenance</li></ul></div>
  <div class="fcol" style="left:676px"><h4>Resources</h4><ul><li>Blog</li><li>Our Team</li><li>Projects</li><li>Faq</li></ul></div>
  <div class="fcol" style="left:836px"><h4>Usage</h4><ul><li>Terms &amp; Conditions</li><li>Privacy Policy</li><li>Refund Policy</li></ul></div>
  <div class="abs" style="left:295px;top:326px;width:192px;height:1px;background:rgba(255,255,255,.35)"></div>
  <div class="abs" style="left:713px;top:326px;width:192px;height:1px;background:rgba(255,255,255,.35)"></div>
  <span class="soc" style="left:533px"></span><span class="soc" style="left:585px"></span><span class="soc" style="left:638px"></span>
  <div class="abs" style="left:0;width:1200px;text-align:center;top:354px;font-size:11px;color:#dfe9e4">Copyright © 2025 Corbel Crest Lighting. All Rights Reserved.</div>
</footer>

</body>
</html>
```